Etiketten-Design für Dankeswein
Zielgruppe
Vo-Lux:
Wir stellen für unsere Kunden einen Dankeswein her. Er soll eine Hommage an die Freundschaft und Partnerschaft sein.
Subtitle, could be, but perhaps not:
When we meet, anything can happen.
Name: Vo-Lux (evtl. Änderung auf KaFol)
Aufgabenstellung
Das Ettikett darf auch bunt sein, aber es sollte vorallem sehr Professionell sein.
Der Wein wird rötlich sein, die Flasche weiss durchsichtig. Es werden wahrscheinlich 0,5l Flaschen.
Die Form des Ettikets, kann noch definiert werden.
Es geht um eine Homage an das Treffen von Menschen und die Freundschaft.
Vo-Lux
Hintergrundinfos, die eher für den Hintergrund, Einarbeitung und kleine Abbildung gedacht sind.
TORVIK: ist eine IT Firma, die von 2 Partnern gegründet wurde. Das Logo sollte mit drauf, evtl. kann man auch sich an diesen Farben orientieren.
Familie Abegg: Die Tiersymbole repräsentieren die beiden Eltern. Das geschwungene H ist das Familienzeichen. Wenn man es rotiert. ähnelt es wieder einem Schmetterling. Vielleicht kann man da grafisch etwas machen?
Das geschwungene H oder die Tiersymbole haben hohen emotionalen Wert. In dem Wappen ist das neue Familiensymbol eingearbeitet in das noch ältere Familienwappen der Familie. Prio hat das geschwungene H
Für das Ettikett gibt es leider rechtliche Pflichtangaben:
TORVIK GmbH
Rindermarktgasse 9 CH-4052 Basel
Erzeugerab füllung:D- RP 7 438 926
A.P.-Nr.7 438 926 XXXX
11,0%vol 50 cl Enthält Sulfite
Deutscher Qualitätswein – Mosel
vo-lux.eu

```html
<!DOCTYPE html>
<html lang="de">
<head>
<meta charset="utf-8">
<title>Danke – Etikett</title>
<link rel="stylesheet" href="https://fonts.googleapis.com/css2?family=Great+Vibes&family=Quicksand:wght@400;500&display=swap">
<style>
  :root {
    --paper: #ffffff;
    --frame: #eef1e4;
    --script-green: #7aa833;
    --script-ghost: #efefef;
    --brand-blue: #4f9cc8;
    --info-grey: #9a9a9a;
  }
  html, body {
    margin: 0;
    padding: 0;
    overflow: hidden;
    background: var(--paper);
  }
  .label {
    position: relative;
    width: 923px;
    height: 1200px;
    overflow: hidden;
    background: var(--paper);
    font-family: "Quicksand", sans-serif;
  }
  .label__frame {
    position: absolute;
    left: 47px;
    top: 47px;
    width: 829px;
    height: 1107px;
    box-sizing: border-box;
    border: 20px solid var(--frame);
  }
  .label__ghost-word {
    position: absolute;
    left: -30px;
    top: 115px;
    margin: 0;
    font-family: "Great Vibes", cursive;
    font-weight: 400;
    font-size: 370px;
    line-height: 1;
    color: var(--script-ghost);
    white-space: nowrap;
  }
  .label__title {
    position: absolute;
    left: 0;
    right: 0;
    top: 195px;
    margin: 0;
    text-align: center;
    font-family: "Great Vibes", cursive;
    font-weight: 400;
    font-size: 255px;
    line-height: 1;
    color: var(--script-green);
    white-space: nowrap;
  }
  .label__brand {
    position: absolute;
    left: 0;
    right: 0;
    top: 832px;
    margin: 0;
    text-align: center;
    font-family: "Quicksand", sans-serif;
    font-weight: 500;
    font-size: 46px;
    letter-spacing: 2px;
    line-height: 1;
    color: var(--brand-blue);
  }
  .label__legal {
    position: absolute;
    left: 0;
    right: 0;
    top: 923px;
    margin: 0;
    text-align: center;
    font-size: 15.5px;
    line-height: 23px;
    color: var(--info-grey);
  }
  .label__legal p {
    margin: 0 0 24px;
  }
</style>
</head>
<body>
  <main class="label">
    <div class="label__frame"></div>
    <div class="label__ghost-word" aria-hidden="true">Danke</div>
    <h1 class="label__title">Danke</h1>
    <p class="label__brand">TORVIK</p>
    <div class="label__legal">
      <p>TORVIK GmbH • Rindermarktgasse 9 CH-4052 Basel</p>
      <p>Erzeugerab füllung:D- RP 7 438 926 • A.P.-Nr.7 438 926 XXXX<br>11,0%vol 50 cl Enthält Sulfite</p>
      <p>Deutscher Qualitätswein – Mosel<br>vo-lux.eu</p>
    </div>
  </main>
</body>
</html>
```